Business Card That Looks Like a Sports Card

Want it to look like a sports trading card. That front should have a baseball player. The back will list our contact info and website info etc.

Contact Information for Business Card

www.prairiegoal.net
gotoPGX.com
Email: dale@prairiegoal.net

Colors

Designer to choose colors to be used in the design.

Requirements
Must have
• Use our current logo and color scheme. Must look like a sports trading card.

```html
<!DOCTYPE html>
<html lang="en">
<head>
<meta charset="utf-8">
<title>Prairie Goal Sports Memorabilia – Business Card</title>
<link rel="stylesheet" href="https://fonts.googleapis.com/css2?family=Oswald:wght@500;600&family=Arimo:wght@400;700&display=swap">
<style>
  :root {
    --navy: #1d2c6c;
    --navy-deep: #15215a;
    --teal: #1fbf95;
    --white: #ffffff;
    --paper: #eeeff1;
    --photo-top: #0d1e45;
    --photo-mid: #1b5a8a;
    --photo-low: #123349;
  }
  * { box-sizing: border-box; margin: 0; padding: 0; }
  html, body { width: 1200px; height: 800px; overflow: hidden; }
  body {
    background: var(--paper);
    display: flex;
    align-items: center;
    justify-content: center;
    gap: 70px;
    font-family: "Arimo", Arial, sans-serif;
  }
  .card {
    position: relative;
    width: 360px;
    height: 630px;
    overflow: hidden;
    box-shadow: 0 6px 18px rgba(0,0,0,0.18);
  }

  /* Front */
  .card-front { background: var(--navy); }
  .card-front .stripe {
    position: absolute; top: 0; bottom: 0; width: 18px; background: var(--teal);
  }
  .card-front .stripe-left { left: 30px; }
  .card-front .stripe-right { right: 30px; }
  .player-photo {
    position: absolute;
    left: 48px; right: 48px; top: 0; height: 470px;
    background: linear-gradient(180deg, var(--photo-top) 0%, var(--photo-mid) 48%, var(--photo-low) 80%, var(--navy-deep) 100%);
  }
  .front-brand {
    position: absolute; left: 48px; right: 48px; top: 500px;
    text-align: center;
    font-family: "Oswald", Impact, sans-serif;
    font-weight: 600;
    color: var(--white);
    text-transform: uppercase;
    line-height: 1.1;
  }
  .front-brand .brand-name { font-size: 38px; letter-spacing: 0.5px; display: block; }
  .front-brand .brand-sub { font-size: 15px; letter-spacing: 1.5px; display: block; margin-top: 2px; }

  /* Back */
  .card-back { background: var(--white); }
  .card-back .stripe {
    position: absolute; top: 0; bottom: 0; width: 12px; background: var(--teal);
  }
  .card-back .stripe-left { left: 20px; }
  .card-back .stripe-right { right: 20px; }
  .card-back .band {
    position: absolute; left: 48px; right: 48px; height: 60px; background: var(--navy);
  }
  .card-back .band-top { top: 0; }
  .card-back .band-bottom { bottom: 0; }
  .info-panel {
    position: absolute; left: 46px; right: 46px; top: 28px; bottom: 28px;
    background: var(--white);
    border: 6px solid var(--teal);
    border-radius: 18px;
    display: flex; flex-direction: column; align-items: center;
    padding-top: 50px;
    text-align: center;
    color: var(--navy);
  }
  .brand-mark {
    display: flex; align-items: center; gap: 10px;
    font-family: "Oswald", Impact, sans-serif;
    font-weight: 600;
    font-size: 30px;
    color: var(--navy);
    text-transform: uppercase;
  }
  .brand-mark .dot { width: 18px; height: 18px; border-radius: 50%; background: var(--navy); }
  .contact-name {
    margin-top: 80px;
    font-family: "Oswald", Impact, sans-serif;
    font-weight: 500;
    font-size: 38px;
    color: var(--teal);
    text-transform: uppercase;
    line-height: 1;
  }
  .contact-email { margin-top: 8px; font-size: 16px; }
  .contact-address { margin-top: 26px; font-size: 17px; line-height: 1.3; }
  .divider-star { margin: 8px 0 4px; }
  .contact-web { font-size: 17px; font-weight: 700; line-height: 1.35; }
</style>
</head>
<body>

  <article class="card card-front">
    <span class="stripe stripe-left"></span>
    <span class="stripe stripe-right"></span>
    <div class="player-photo" role="img" aria-label="Photo of a baseball batter in a pinstripe uniform in a lit stadium at night"></div>
    <div class="front-brand">
      <span class="brand-name">Prairie Goal</span>
      <span class="brand-sub">Sports Memorabilia</span>
    </div>
  </article>

  <article class="card card-back">
    <span class="stripe stripe-left"></span>
    <span class="stripe stripe-right"></span>
    <span class="band band-top"></span>
    <span class="band band-bottom"></span>
    <div class="info-panel">
      <div class="brand-mark"><span class="dot"></span>Prairie Goal</div>
      <h1 class="contact-name">Sam Corwell</h1>
      <p class="contact-email">dale@prairiegoal.net</p>
      <p class="contact-address">4820 Meadowlark Lane,<br>Suite 310, Carmel<br>Indiana 46032</p>
      <svg class="divider-star" width="16" height="16" viewBox="0 0 24 24" aria-hidden="true">
        <polygon fill="#1fbf95" points="12,1 15,9 23,9 16.5,14 19,22 12,17 5,22 7.5,14 1,9 9,9"/>
      </svg>
      <p class="contact-web">www.prairiegoal.net<br>gotoPGX.com</p>
    </div>
  </article>

</body>
</html>
```